I am a pastry chef and just started my own business. I make all sorts of pastries: french macarons, petit fours, artisan chocolates, artisan bread, and they can be ordered on the website. I'm obsessed with Wonderland, so I'd like to have a logo & a background that incorporate that, something whimsical. I was thinking of a white rabbit wearing a chef toque - maybe he could have a monocle on. The logo could go on one side of the business card with "Sugar Fox Patisserie Co" on a banner of some sort at the bottom, and the contact & info could go on the other side. I'd like a really light color as the background, maybe a really light yellow.

Industry/Entity Type

Chef

Contact Information for Business Card

Sugar Fox Patisserie Co
Mira Delcour Penhale
sugarfoxpatisserieco.shopvaleo.example
sugarfoxpatisserieco@mailvaleo.example
514-83-2071

```html
<!DOCTYPE html>
<html lang="en">
<head>
<meta charset="utf-8">
<title>Sugar Fox Patisserie Co — Business Card</title>
<link rel="stylesheet" href="https://fonts.googleapis.com/css2?family=Archivo+Black&family=Arimo:ital,wght@0,400;0,700;1,700&display=swap">
<style>
  :root {
    --page-bg: #ecebe6;
    --card-yellow: #fff200;
    --card-yellow-light: #fffbd0;
    --stripe-blue: #1e9be0;
    --badge-blue-light: #e6f5fc;
    --badge-blue: #8fd0ef;
    --panel-green: #b9d66a;
    --panel-green-light: #f7fbe8;
    --ring-green: #e4f0c0;
    --ink: #111111;
    --brand-ink: #1b2a4a;
  }
  * { margin: 0; padding: 0; box-sizing: border-box; }
  html, body { width: 1200px; height: 831px; overflow: hidden; }
  body {
    background: var(--page-bg);
    position: relative;
    font-family: "Arimo", Arial, sans-serif;
  }
  .card {
    position: absolute;
    width: 620px;
    height: 354px;
    overflow: hidden;
    box-shadow: 0 6px 18px rgba(0,0,0,0.18);
  }
  .card--front {
    left: 60px; top: 50px;
    background: radial-gradient(ellipse 55% 60% at 50% 45%, var(--card-yellow-light) 0%, var(--card-yellow) 75%);
  }
  .card--back {
    left: 520px; top: 434px;
    background: var(--card-yellow);
  }
  .stripes { position: absolute; left: 0; top: 0; width: 620px; height: 354px; }
  .logo {
    position: absolute;
    display: flex;
    flex-direction: column;
    align-items: center;
    gap: 12px;
  }
  .logo__badge {
    border-radius: 50%;
    background: radial-gradient(circle at 50% 40%, var(--badge-blue-light) 0%, var(--badge-blue) 100%);
  }
  .logo__name {
    font-family: "Arimo", Arial, sans-serif;
    font-weight: 700;
    font-size: 17px;
    color: var(--brand-ink);
    white-space: nowrap;
  }
  .card--front .logo { left: 210px; top: 70px; width: 220px; }
  .card--front .logo__badge { width: 150px; height: 150px; }
  .card--back .logo { left: 350px; top: 70px; width: 260px; }
  .card--back .logo__badge { width: 160px; height: 160px; }

  .contact-panel {
    position: absolute;
    left: -300px; top: -200px;
    width: 640px; height: 640px;
    border-radius: 50%;
    background: var(--ring-green);
  }
  .contact-panel::after {
    content: "";
    position: absolute;
    inset: 16px;
    border-radius: 50%;
    background: radial-gradient(circle at 68% 62%, var(--panel-green-light) 0%, var(--panel-green) 70%);
  }
  .contact {
    position: absolute;
    left: 34px; top: 78px;
    color: var(--ink);
  }
  .contact__name {
    font-family: "Archivo Black", Arial, sans-serif;
    font-size: 22px;
    font-weight: 400;
    text-decoration: underline;
    text-decoration-thickness: 2px;
    text-underline-offset: 3px;
    margin-bottom: 24px;
  }
  .contact__label {
    font-weight: 700;
    font-style: italic;
    font-size: 16px;
    margin-bottom: 10px;
  }
  .contact__list { list-style: none; font-size: 13px; line-height: 1.35; }
</style>
</head>
<body>

  <section class="card card--front" aria-label="Business card front">
    <svg class="stripes" viewBox="0 0 620 354" aria-hidden="true">
      <g fill="var(--stripe-blue)">
        <polygon points="0,186 170,186 162,204 0,204"/>
        <polygon points="178,186 222,186 214,204 170,204"/>
        <polygon points="418,150 452,150 444,168 410,168"/>
        <polygon points="460,150 490,150 482,168 452,168"/>
        <polygon points="498,150 620,150 620,168 490,168"/>
      </g>
    </svg>
    <div class="logo">
      <div class="logo__badge" role="img" aria-label="Brand mascot illustration area"></div>
      <span class="logo__name">Sugar Fox Patisserie Co</span>
    </div>
  </section>

  <section class="card card--back" aria-label="Business card back">
    <div class="contact-panel" aria-hidden="true"></div>
    <div class="contact">
      <h1 class="contact__name">Mira Delcour Penhale</h1>
      <p class="contact__label">Contact :</p>
      <ul class="contact__list">
        <li>sugarfoxpatisserieco.shopvaleo.example</li>
        <li>sugarfoxpatisserieco@mailvaleo.example</li>
        <li>514-83-2071</li>
      </ul>
    </div>
    <div class="logo">
      <div class="logo__badge" role="img" aria-label="Brand mascot illustration area"></div>
      <span class="logo__name">Sugar Fox Patisserie Co</span>
    </div>
  </section>

</body>
</html>
```